Beauty Salon Treatment Menu & Pricing

We need a Treatment Pricelist/ Brochure made to hand out to potential & existing customers! Meadowlark Body & Makeup is a small friendly beauty salon focused on the beauty essentials such as waxing, spray tanning, facials & makeup. We have a webpage with our colour theme and style and we would like to brochure to tie in.
www.meadowlarkbodyandmakeup.com.au.
We like a brochure that is clean, simple and easy to read.

Industry/Entity Type

Beauty Salon

```html
<!DOCTYPE html>
<html lang="en">
<head>
<meta charset="utf-8">
<title>Meadowlark Body &amp; Makeup – Facials</title>
<link rel="stylesheet" href="https://fonts.googleapis.com/css2?family=Didact+Gothic&display=swap">
<style>
  :root {
    --brand-red: #e8202e;
    --ink: #2e2e2e;
    --paper: #ffffff;
  }
  * { margin: 0; padding: 0; box-sizing: border-box; }
  html, body { width: 846px; height: 1200px; overflow: hidden; background: var(--paper); }
  .menu-page {
    position: relative;
    width: 846px;
    height: 1200px;
    font-family: "Didact Gothic", "Century Gothic", sans-serif;
    color: var(--ink);
  }
  .side-band {
    position: absolute;
    left: 0; top: 0;
    width: 103px; height: 1200px;
    background: var(--brand-red);
  }
  .side-band__title {
    position: absolute;
    left: 52px; top: 172px;
    transform: translate(-50%, -50%) rotate(-90deg);
    color: var(--paper);
    font-size: 62px;
    letter-spacing: 2px;
    white-space: nowrap;
    line-height: 1;
  }
  .treatment {
    position: absolute;
    left: 150px;
    width: 660px;
  }
  .treatment__head {
    position: relative;
    color: var(--brand-red);
    font-size: 18.5px;
    line-height: 22px;
    text-transform: uppercase;
    margin-bottom: 1px;
  }
  .treatment__price {
    position: absolute;
    left: 510px; top: 0;
  }
  .treatment__body {
    font-size: 13.6px;
    line-height: 20.8px;
  }
  .addons {
    position: absolute;
    left: 150px; top: 1012px;
    width: 660px;
  }
  .addons__list {
    list-style: none;
    font-size: 13.6px;
    line-height: 20px;
  }
  .addons__list li { position: relative; }
  .addons__price { position: absolute; left: 320px; top: 0; }
</style>
</head>
<body>
<main class="menu-page">
  <aside class="side-band"><h1 class="side-band__title">FACIALS</h1></aside>

  <section class="treatment" style="top:57px">
    <h2 class="treatment__head">Quick Fix My Skin <span class="treatment__price">65.00</span></h2>
    <p class="treatment__body">Allow 30 minutes. &nbsp;“HELP! My skin has gone wild and is doing all sorts of unusual things!”<br>With this express facial a combination of advanced DERMA NOVA products best suited to treat your current skin condition will be used. Includes an exfoliation, active serums and a powerful face mask.</p>
  </section>

  <section class="treatment" style="top:151px">
    <h2 class="treatment__head">Glycolic Peel Treatment <span class="treatment__price" style="left:515px">55.00</span></h2>
    <p class="treatment__body">Buy 4 and get the 5th treatment free (1 treatment p/w)<br>Allow 20 minutes. An active treatment combining the powerful effects of Glycolic Acid and Vitamin C to refine the skins appearance and texture, balance irregularities in skin tone and pigmentation, counteract the effect of acne, including scarring and reduce blackheads and other blemishes.</p>
  </section>

  <section class="treatment" style="top:266px">
    <h2 class="treatment__head">Glycolic Microdermabrasion Treatment <span class="treatment__price">100.00</span></h2>
    <p class="treatment__body">Allow 45 minutes. This is a highly active treatment to target the skins imperfections and overall complexion. We incorporate the use of the microdermabrasion scrub and the skin refining mask to enhance the effects of the glycolic peel treatment as well as lengthen the treatment to be more relaxing and effective.</p>
  </section>

  <section class="treatment" style="top:381px">
    <h2 class="treatment__head">Clear Skin Facial <span class="treatment__price">80.00</span></h2>
    <p class="treatment__body">Allow 45 mins. A deep cleansing facial designed to help manage and treat oily, acne and pustular skin. The treatment uses a combination of ingredients including Vitamin A, Tea Tree, multi-fruid acids, minerals and deep cleansing clays.</p>
  </section>

  <section class="treatment" style="top:476px">
    <h2 class="treatment__head">Rebalancing Vitamin A Facial <span class="treatment__price">90.00</span></h2>
    <p class="treatment__body">Allow 60 mins. A relaxing treatment for combination skin types, to detox, purify and heal the skin. The treatment incorporates the use of Vitamin A, Zinc Oxide, Stem cells, Lotus Flower liposomes, Green Tea and Ginkgo Biloba.</p>
  </section>

  <section class="treatment" style="top:570px">
    <h2 class="treatment__head">Marine Radiance Facial <span class="treatment__price">100.00</span></h2>
    <p class="treatment__body">Allow 60 mins. This gentle and rehydrating treatment is suitable for most skin types, to restore softness and radiance to the skins complexion. Oxygenating and strengthening, incorporating marine extracts, collagen and elastin. A perfect facial for the Bride-to-be! (add a Glycolic peel to enhance the benefits)</p>
  </section>

  <section class="treatment" style="top:686px">
    <h2 class="treatment__head">Anti Stress, Sensitive Skin Treatment <span class="treatment__price">100.00</span></h2>
    <p class="treatment__body">Allow 60 mins. Perfect for skin that is prone to redness, irritation, flakiness and inflammation. This treatment is super relaxing whilst using Boswellic Acid (a plant derived natural anti-inflammatory) along with cehami to soothe the skin. Great for anyone who suffers from eczema, dermatitis and psoriasis. Skin will look and feel calmer.</p>
  </section>

  <section class="treatment" style="top:801px">
    <h2 class="treatment__head">Anti Ageing Hydra Restore Facial <span class="treatment__price">120.00</span></h2>
    <p class="treatment__body">Allow 60 mins. A beautiful hot oil infusion treatment that uses 100% natural vitamins and oils. Great for any sign of dehydration, dryness and wrinkles. The skin will look younger, healthier, radiant and feel amazing! Perfect for anyone who has completed a course of the glycolic peel treatments.</p>
  </section>

  <section class="treatment" style="top:896px">
    <h2 class="treatment__head">Firming Lift Facial <span class="treatment__price">150.00</span></h2>
    <p class="treatment__body">Allow 60 mins. The most luxurious and restorative facial treatment to firm, strengthen and oxygenate the skin. Using a high quality marine derived collagen, elastin and pearl extract, this facial treatment is ideal for anyone losing skin firmness and elasticity. Also great for delicate and fragile skin. Includes caviar &amp; pearl eye treatment.</p>
  </section>

  <section class="addons">
    <h2 class="treatment__head">Facial Add Ons</h2>
    <p class="treatment__body">(Incorporate any of the following into a your facial treatment for a small cost).</p>
    <ul class="addons__list">
      <li>Glycolic Peel <span class="addons__price">20.00</span></li>
      <li>Firming Lift Caviar &amp; Pearl Eye Treatment <span class="addons__price">20.00</span></li>
      <li>Firming Lift Neck &amp; Bust Treatment <span class="addons__price">20.00</span></li>
      <li>Mini Pedicure (file &amp; Polish) <span class="addons__price">30.00</span></li>
    </ul>
  </section>
</main>
</body>
</html>
```